Modern business card design for professional copywriter

I'd like a business card design that I can use to have my cards printed out by plink.com as a squared corners business card (see artwork and design guidelines here: https://help.plink.com/hc/en-gb/sections/300481726-PLINK-Product-Templates)

The design should be clean and modern and reflect the colours, tone and branding on my website: https://noravestrel.com.au

Target Market(s)

Professionals, B2B small business owners

Industry/Entity Type

Business

Contact Information for Business Card

Nora Vestrel
m: 0427 593 864
e: nora@noravestrel.com.au
w: noravestrel.com.au

Font styles to use
Sans Serif

Requirements
Must have
• Tagline: "Smart copywriting for clever business people"
• Brand colours: fd8000, 009984, 666666 and black
Nice to have

```html
<!DOCTYPE html>
<html lang="en">
<head>
<meta charset="utf-8">
<title>Nora Vestrel – Business Card</title>
<link rel="stylesheet" href="https://fonts.googleapis.com/css2?family=Open+Sans:ital,wght@0,400;0,600;1,700&display=swap">
<style>
  :root {
    --brand-green: #2ed16b;
    --brand-orange: #fd6a00;
    --brand-grey: #5c6266;
    --card-white: #ffffff;
    --canvas-bg: #ffffff;
    --card-border: #555555;
    --text-font: "Open Sans", Arial, sans-serif;
  }
  * { box-sizing: border-box; margin: 0; padding: 0; }
  html, body {
    width: 1200px;
    height: 1200px;
    overflow: hidden;
    background: var(--canvas-bg);
    font-family: var(--text-font);
  }
  .canvas {
    position: relative;
    width: 1200px;
    height: 1200px;
  }
  .card {
    position: absolute;
    left: 310px;
    width: 612px;
    height: 340px;
  }
  .card--front {
    top: 193px;
    background: var(--card-white);
    border: 1px solid var(--card-border);
  }
  .card--back {
    top: 629px;
    background: var(--brand-green);
    color: var(--card-white);
  }

  /* Front */
  .front-brand {
    position: absolute;
    top: 112px;
    left: 0;
    right: 0;
    display: flex;
    flex-direction: column;
    align-items: center;
  }
  .brand-line {
    display: flex;
    align-items: center;
    gap: 14px;
  }
  .brand-mark {
    width: 22px;
    height: 22px;
    border-radius: 50%;
    background: var(--brand-orange);
  }
  .brand-name {
    font-weight: 600;
    font-size: 54px;
    line-height: 1;
    color: var(--brand-green);
    letter-spacing: -0.5px;
  }
  .brand-role {
    align-self: flex-end;
    margin-right: 96px;
    margin-top: 4px;
    font-size: 15px;
    letter-spacing: 5px;
    color: var(--brand-grey);
  }
  .tagline-band {
    position: absolute;
    top: 245px;
    left: -2px;
    right: -2px;
    height: 29px;
    background: var(--brand-green);
    display: flex;
    align-items: center;
    justify-content: center;
  }
  .tagline {
    font-style: italic;
    font-weight: 700;
    font-size: 17px;
    color: var(--card-white);
  }

  /* Back */
  .back-brand {
    position: absolute;
    top: 44px;
    left: 38px;
    display: flex;
    flex-direction: column;
  }
  .back-brand .brand-line { gap: 8px; }
  .back-brand .brand-mark {
    width: 10px;
    height: 10px;
    background: var(--card-white);
  }
  .back-brand .brand-name {
    font-size: 27px;
    color: var(--card-white);
    letter-spacing: -0.3px;
  }
  .back-brand .brand-role {
    margin: 2px 0 0 0;
    font-size: 8px;
    letter-spacing: 2.6px;
    color: var(--card-white);
  }
  .contact {
    position: absolute;
    right: 36px;
    bottom: 22px;
    text-align: right;
    font-style: normal;
    font-size: 20px;
    line-height: 26px;
  }
</style>
</head>
<body>
<main class="canvas">
  <section class="card card--front" aria-label="Business card front">
    <div class="front-brand">
      <div class="brand-line">
        <span class="brand-mark"></span>
        <span class="brand-name">Nora Vestrel</span>
      </div>
      <span class="brand-role">COPYWRITER</span>
    </div>
    <div class="tagline-band">
      <p class="tagline">Smart copywriting for clever business people</p>
    </div>
  </section>

  <section class="card card--back" aria-label="Business card back">
    <div class="back-brand">
      <div class="brand-line">
        <span class="brand-mark"></span>
        <span class="brand-name">Nora Vestrel</span>
      </div>
      <span class="brand-role">COPYWRITER</span>
    </div>
    <address class="contact">
      <div class="contact-name">Nora Vestrel</div>
      <div class="contact-phone">m: 0427 593 864</div>
      <div class="contact-email">e: nora@noravestrel.com.au</div>
      <div class="contact-web">w: noravestrel.com.au</div>
    </address>
  </section>
</main>
</body>
</html>
```